Website Design for Freeze-Dried Food Manufacturing Company (Pet Food & Agri-Food)

We are looking for a high-level web designer to create a clean, modern, premium website design for Tarquel, a freeze-dried food manufacturing company operating in both the pet food and agri-food space.
This is not a basic website build β we are looking for a designer who understands brand positioning, layout, and user flow, not just visuals.
π― Project Objective
Design a website that:
Clearly communicates our capabilities and value proposition
Feels premium, credible, and product-driven
Guides users through a simple, intuitive journey
Clean and Crips
A critical requirement is clearly separating:
π Pet Food
π Agri-Food
These must feel like two distinct pathways within the same brand experience.
We have attached detailed documents outlining structure, layout, and messaging. These should be followed closely.
π What Success Looks Like
A high-impact homepage with strong visual hierarchy
Clear entry points into Pet Food and Agri-Food
Clean, intentional layout (not cluttered or template-like)
Thoughtful spacing, typography, and flow
A design that feels considered and elevated, not generic
π¨ Design Direction
We are aiming for a:
Minimal, premium aesthetic
Warm, natural color palette (creams, browns, muted tones)
Ingredient and product-focused visuals
Avoid:
Overly corporate / industrial styles
Generic SaaS-style layouts
Busy or over-designed interfaces
End Goal
A website that immediately communicates:
Who we are
What we do
Why weβre different
In a way that feels premium, clear, and easy to navigate.
Link to current website: https://tarquelfoods.example/
https://tarquelhealth.example/wp-admin/

```html
<!DOCTYPE html>
<html lang="en">
<head>
<meta charset="utf-8">
<title>Tarquel — Freeze-Dried Manufacturing</title>
<link href="https://fonts.googleapis.com/css2?family=Outfit:wght@400;500;600;700;800&family=Figtree:wght@400;500;600&display=swap" rel="stylesheet">
<style>
:root{
  --cream:#f4f0e7;
  --white:#ffffff;
  --brown:#4b2e26;
  --brown-deep:#3a2721;
  --olive:#7c8568;
  --olive-light:#8f9a7c;
  --ink:#1f1b19;
  --text:#2c2724;
  --muted:#6f6760;
  --footer:#252120;
  --rule:#8a7d72;
  --footer-label:#a39a90;
}
*{box-sizing:border-box;margin:0;padding:0}
html,body{width:1200px;height:3206px;overflow:hidden}
body{background:var(--cream);font-family:"Figtree",sans-serif;color:var(--text);position:relative}
.abs{position:absolute}
h1,h2,h3{font-family:"Outfit",sans-serif;font-weight:700;letter-spacing:-0.03em;color:var(--ink)}
.btn{display:inline-flex;align-items:center;gap:10px;border-radius:30px;background:var(--olive);color:#fff;font-family:"Outfit",sans-serif;font-weight:600;font-size:15px;text-decoration:none;justify-content:center}
.btn svg{width:14px;height:14px}
.swoosh{display:block;width:110px;height:12px}

/* top bar */
.topbar{top:0;left:0;width:1200px;height:28px;background:var(--brown-deep);color:#fff;font-size:12px;display:flex;justify-content:flex-end;align-items:center;gap:18px;padding-right:144px}
.topbar span{display:flex;align-items:center;gap:6px}
.nav{top:28px;left:0;width:1200px;height:70px;background:var(--white);display:flex;align-items:center;padding:0 142px}
.brand{font-family:"Outfit",sans-serif;font-weight:400;font-size:44px;color:#a3603e;letter-spacing:0.02em;text-decoration:none}
.menu{margin-left:auto;display:flex;gap:30px;list-style:none;font-family:"Outfit",sans-serif;font-size:15px;align-items:center}
.menu li{color:var(--ink)}
.menu .active{background:var(--olive);color:#fff;border-radius:14px;padding:3px 8px}

/* hero */
.hero{top:98px;left:0;width:1200px;height:630px}
.hero-copy{top:192px;left:142px;width:560px;color:#fff;z-index:2}
.hero-copy h1{color:#fff;font-size:46px;line-height:56px;font-weight:800}
.hero-copy p{margin-top:20px;font-size:16px;line-height:28px;width:530px}
.hero-copy .btn{margin-top:34px;width:176px;height:52px;font-size:16px;background:var(--olive-light)}

/* who */
.circle{border-radius:50%}
.who{top:745px;left:673px;width:385px}
.who h2{font-size:32px}
.who .swoosh{margin:10px 0 0 0}
.who .lead{margin-top:18px;font-size:17px;line-height:29px;color:var(--text)}
.who .body{margin-top:16px;font-size:13.5px;line-height:23px;color:var(--muted);text-align:justify}
.who .btn{margin-top:40px;width:152px;height:44px}

.center{left:0;width:1200px;text-align:center;z-index:3}
.center h2{font-size:32px}
.center .swoosh{margin:8px auto 0}
.center p.intro{font-size:17px;line-height:29px;margin:20px auto 0;width:900px}

/* pathways */
.panel{top:1428px;height:612px;width:600px;color:#fff;text-align:center}
.panel.agri{left:0;background:linear-gradient(160deg,#5e3e31,#4a2f26 60%,#5a3b2e)}
.panel.pet{left:600px;background:linear-gradient(200deg,#97a083,#7f8a6c 60%,#8d977a)}
.panel .icon{width:80px;height:80px;border-radius:50%;margin:157px auto 0;display:flex;align-items:center;justify-content:center}
.agri .icon{background:var(--olive-light)}
.pet .icon{background:var(--brown)}
.panel .icon svg{width:42px;height:42px}
.panel h3{color:#fff;font-size:35px;margin-top:18px}
.panel p{font-size:14px;line-height:23px;margin:18px auto 0;width:380px}
.panel .btn{margin-top:26px;width:152px;height:44px;font-size:14px}
.pet .btn{background:var(--brown)}
.wave{z-index:1}

.features{top:2209px;left:142px;width:916px;display:flex;justify-content:space-between}
.feature{text-align:center;width:200px;color:var(--muted);font-size:16px}
.feature .disc{width:96px;height:96px;border-radius:50%;background:var(--brown);margin:0 auto 18px;display:flex;align-items:center;justify-content:center}
.feature .disc svg{width:54px;height:54px}

/* footer */
.footer{top:2780px;left:0;width:1200px;height:426px;background:var(--footer)}
.fcol{color:#fff;z-index:2}
.fcol h4{font-family:"Outfit",sans-serif;font-weight:400;font-size:16px;letter-spacing:0.01em;color:#fff}
.contact{top:2862px;left:142px}
.citem{display:flex;gap:10px;margin-top:16px}
.citem svg{width:14px;height:14px;margin-top:2px;flex:none}
.citem small{display:block;font-size:11px;color:var(--footer-label);letter-spacing:0.03em}
.citem span{font-size:14px;color:#fff}
.links{top:2862px;left:493px}
.links ul{list-style:none;margin-top:14px;font-size:14px;line-height:25.5px;color:#fff}
.news{top:2862px;left:757px;width:300px}
.news p{font-size:13px;line-height:20px;margin-top:14px;color:#fff}
.field{margin-top:18px;width:298px;height:44px;border:1px solid #c9c1b8;border-radius:22px;display:flex;align-items:center;padding-left:18px;gap:6px;font-size:11px;color:#fff}
.news .btn{margin-top:16px;width:128px;height:40px}
.copy{top:3102px;left:0;width:1200px;text-align:center;font-size:14px;color:#fff;z-index:2}
.social{top:3141px;left:546px;display:flex;gap:8px;z-index:2}
.social span{width:28px;height:28px;border-radius:50%;background:#fff}
.social span.mid{background:var(--olive)}
</style>
</head>
<body>

<div class="abs topbar">
  <span><svg width="12" height="10" viewBox="0 0 12 10"><rect x="0.5" y="0.5" width="11" height="9" fill="none" stroke="#fff"/><path d="M1 1l5 4 5-4" fill="none" stroke="#fff"/></svg>Sales: sales@tarquelfoods.example</span>
  <span><svg width="11" height="11" viewBox="0 0 24 24"><path d="M6.6 10.8a15 15 0 006.6 6.6l2.2-2.2a1 1 0 011-.25 11.4 11.4 0 003.6.6 1 1 0 011 1V20a1 1 0 01-1 1A17 17 0 013 4a1 1 0 011-1h3.5a1 1 0 011 1c0 1.25.2 2.45.6 3.6a1 1 0 01-.25 1z" fill="#fff"/></svg>1.800.55TARQL (82775)</span>
</div>

<header class="abs nav">
  <a class="brand" href="https://tarquelfoods.example/">Tarquel</a>
  <ul class="menu">
    <li class="active">HOME</li><li>ABOUT US</li><li>WAREHOUSES</li><li>AGRIFOOD</li><li>PHARMA</li><li>LIFE-SCIENCE</li><li>CONTACT</li>
  </ul>
</header>

<svg class="abs hero" viewBox="0 0 1200 630" role="img" aria-label="Photo of workers in hairnets processing food beside a large stainless steel freeze-drying vessel">
  <defs><linearGradient id="heroG" x1="0" x2="1" y1="0" y2="0">
    <stop offset="0" stop-color="#3e3d3b"/><stop offset="0.5" stop-color="#5a5856"/><stop offset="1" stop-color="#8b8986"/></linearGradient></defs>
  <path d="M0 0H1200V475Q600 623 0 475Z" fill="url(#heroG)"/>
</svg>
<div class="abs hero-copy">
  <h1>Freeze-Dried<br>Manufacturing, Built<br>for Modern Food Brands.</h1>
  <p>Tarquel enables providers and brands in the agrifood, fruit, and petfood business to find paths to domestic and international markets.</p>
  <a class="btn" href="#">Get Started <svg viewBox="0 0 14 14"><path d="M1 7h11M8 3l4 4-4 4" fill="none" stroke="#fff" stroke-width="1.5"/></svg></a>
</div>

<div class="abs circle" style="left:-97px;top:655px;width:480px;height:480px;background:linear-gradient(160deg,#cbd3de,#e7d7c1 55%,#7f8a8d)" role="img" aria-label="City skyline with tall glass towers"></div>
<div class="abs circle" style="left:382px;top:686px;width:190px;height:190px;background:linear-gradient(180deg,#d9d4cb,#8e8b86)" role="img" aria-label="Three team members at a trade show"></div>
<div class="abs circle" style="left:256px;top:883px;width:342px;height:342px;background:linear-gradient(170deg,#c9cfd5,#9aa3aa 55%,#3e79c4);border:4px solid var(--cream)" role="img" aria-label="Stainless freeze-drying chamber in a clean room with blue floor"></div>

<section class="abs who">
  <h2>Who We Are</h2>
  <svg class="swoosh" viewBox="0 0 110 12"><path d="M2 10Q55-4 108 10" fill="none" stroke="var(--rule)" stroke-width="1.5"/></svg>
  <p class="lead">Cold Chain Storage, Processing, Packaging and Supply Chain Services.</p>
  <p class="body">TARQUEL specializes in combining processing and packaging, with COLD CHAIN warehouse and distribution services for the Agrifood, Pharmaceutical and Life-Science industries. Tarquel has strategically positioned warehouses across Canada and has international partners for global exports and distribution.</p>
  <a class="btn" href="#">Read More <svg viewBox="0 0 14 14"><path d="M1 7h11M8 3l4 4-4 4" fill="none" stroke="#fff" stroke-width="1.5"/></svg></a>
</section>

<div class="abs panel agri" role="img" aria-label="Dark background of bowls of grains and vegetables">
  <div class="icon"><svg viewBox="0 0 42 42" fill="none" stroke="#fff" stroke-width="1.6"><path d="M11 12h20l3 24H8z"/><path d="M15 12c0-4 12-4 12 0"/><path d="M21 18v14M21 22l-4-2M21 22l4-2M21 27l-4-2M21 27l4-2"/></svg></div>
  <h3>Agri Food</h3>
  <p>Advanced freeze-drying solutions for ingredient suppliers, food innovators, and agricultural partners.</p>
  <a class="btn" href="#">Learn More <svg viewBox="0 0 14 14"><path d="M1 7h11M8 3l4 4-4 4" fill="none" stroke="#fff" stroke-width="1.5"/></svg></a>
</div>
<div class="abs panel pet" role="img" aria-label="Muted green background of a bowl of pet kibble">
  <div class="icon"><svg viewBox="0 0 42 42" fill="none" stroke="#fff" stroke-width="1.6"><path d="M12 8h18l3 28H9z"/><path d="M12 14h18"/><circle cx="21" cy="24" r="5"/><path d="M6 36h30"/></svg></div>
  <h3>Pet Food</h3>
  <p>Premium freeze-dried manufacturing for modern pet brands focused on nutrition, quality, and functional ingredients.</p>
  <a class="btn" href="#">Learn More <svg viewBox="0 0 14 14"><path d="M1 7h11M8 3l4 4-4 4" fill="none" stroke="#fff" stroke-width="1.5"/></svg></a>
</div>
<svg class="abs wave" style="top:1428px;left:0" width="1200" height="100" viewBox="0 0 1200 100"><path d="M0 0H1200V4Q600 148 0 4Z" fill="var(--cream)"/></svg>
<svg class="abs wave" style="top:1940px;left:0" width="1200" height="100" viewBox="0 0 1200 100"><path d="M0 100H1200V90Q600-48 0 90Z" fill="var(--cream)"/></svg>

<section class="abs center" style="top:1290px">
  <h2>What We Do</h2>
  <svg class="swoosh" viewBox="0 0 110 12"><path d="M2 10Q55-4 108 10" fill="none" stroke="var(--rule)" stroke-width="1.5"/></svg>
  <p class="intro" style="margin-top:16px">Tarquel partners with innovative brands across pet food and agri-food to deliver premium freeze-dried products with precision, consistency, and ingredient integrity.</p>
</section>

<section class="abs center" style="top:2032px">
  <h2>Why we’re Different</h2>
  <svg class="swoosh" viewBox="0 0 110 12"><path d="M2 10Q55-4 108 10" fill="none" stroke="var(--rule)" stroke-width="1.5"/></svg>
  <p class="intro">Tarquel partners with innovative brands across pet food and agri-food to deliver premium freeze-dried products with precision, consistency, and ingredient integrity.</p>
</section>

<div class="abs features">
  <div class="feature"><div class="disc"><svg viewBox="0 0 54 54" fill="none" stroke="#fff" stroke-width="1.8"><path d="M27 6l8 3v6c0 5-4 8-8 9-4-1-8-4-8-9V9z"/><path d="M23 15l3 3 5-5"/><path d="M6 32l10-4 8 4 6-2 8 3 10-3M14 34l8 8 4-2 4 3 4-2 6-5"/></svg></div>Ingredient Integrity</div>
  <div class="feature"><div class="disc"><svg viewBox="0 0 54 54" fill="none" stroke="#fff" stroke-width="1.8"><path d="M8 8h38M16 8v8h22V8M27 16v6"/><rect x="18" y="26" width="8" height="12"/><rect x="28" y="26" width="8" height="12"/><rect x="8" y="38" width="38" height="6"/></svg></div>Precision Manufacturing</div>
  <div class="feature"><div class="disc"><svg viewBox="0 0 54 54" fill="none" stroke="#fff" stroke-width="1.8"><rect x="17" y="17" width="20" height="20" transform="rotate(45 27 27)"/><path d="M8 10h12v10M46 44H34V34M10 46V34h10M44 8v12H34"/></svg></div>Scalable Partnership</div>
  <div class="feature"><div class="disc"><svg viewBox="0 0 54 54" fill="none" stroke="#fff" stroke-width="1.8"><circle cx="30" cy="16" r="8"/><path d="M26 16l3 3 5-5"/><path d="M6 34h8v12H6zM14 36h10l6 3h-8M14 44h16l16-10-4-3-12 6"/></svg></div>Collaborative Approach</div>
</div>
<a class="abs btn" style="top:2390px;left:524px;width:152px;height:43px" href="#">Read More <svg viewBox="0 0 14 14"><path d="M1 7h11M8 3l4 4-4 4" fill="none" stroke="#fff" stroke-width="1.5"/></svg></a>

<section class="abs center" style="top:2508px">
  <h2>Built on Consistency. Trusted for Quality.</h2>
  <svg class="swoosh" viewBox="0 0 110 12"><path d="M2 10Q55-4 108 10" fill="none" stroke="var(--rule)" stroke-width="1.5"/></svg>
  <p class="intro" style="font-size:13.5px;line-height:23px;color:var(--muted);width:920px;margin-top:22px">Our manufacturing standards are designed to support premium products from development through production. Tarquel prioritizes process control, ingredient integrity, and reliable execution to help partners confidently scale.</p>
  <a class="btn" style="margin-top:28px;width:160px;height:43px" href="#">Get in Touch <svg viewBox="0 0 14 14"><path d="M1 7h11M8 3l4 4-4 4" fill="none" stroke="#fff" stroke-width="1.5"/></svg></a>
</section>

<footer class="abs footer"></footer>
<svg class="abs" style="top:2780px;left:0" width="1200" height="90" viewBox="0 0 1200 90"><path d="M0 0H1200V83Q600-65 0 83Z" fill="var(--cream)"/></svg>

<div class="abs fcol contact">
  <h4>CONTACT US</h4>
  <div class="citem"><svg viewBox="0 0 24 24"><path d="M6.6 10.8a15 15 0 006.6 6.6l2.2-2.2a1 1 0 011-.25 11.4 11.4 0 003.6.6 1 1 0 011 1V20a1 1 0 01-1 1A17 17 0 013 4a1 1 0 011-1h3.5a1 1 0 011 1c0 1.25.2 2.45.6 3.6a1 1 0 01-.25 1z" fill="#8f9a7c"/></svg><div><small>PHONE</small><span>1.800.55TARQL (82775)</span></div></div>
  <div class="citem"><svg viewBox="0 0 14 14"><rect x="0.5" y="2" width="13" height="10" fill="#8f9a7c"/><path d="M1 2.5l6 5 6-5" fill="none" stroke="#252120"/></svg><div><small>EMAIL</small><span>sales@tarquelfoods.example</span></div></div>
  <div class="citem"><svg viewBox="0 0 14 14"><path d="M7 1a4.5 4.5 0 00-4.5 4.5C2.5 9 7 13 7 13s4.5-4 4.5-7.5A4.5 4.5 0 007 1z" fill="#8f9a7c"/><circle cx="7" cy="5.5" r="1.6" fill="#252120"/></svg><div><small>LOCATION</small><span>ap@tarquelfoods.example</span></div></div>
</div>
<div class="abs fcol links">
  <h4>QUICK LINKS</h4>
  <ul><li>Home</li><li>About Us</li><li>Warehouses</li><li>Agrifood</li><li>Pharma</li><li>Life-Science</li><li>Contact</li></ul>
</div>
<div class="abs fcol news">
  <h4>SUBSCRIBE OUR NEWSLETTER</h4>
  <p>Sign-up and subscribe to our email list to receive important updates!</p>
  <div class="field"><svg width="11" height="9" viewBox="0 0 12 10"><rect x="0.5" y="0.5" width="11" height="9" fill="none" stroke="#fff"/><path d="M1 1l5 4 5-4" fill="none" stroke="#fff"/></svg>Enter Email Address</div>
  <a class="btn" href="#">Subscribe</a>
</div>
<div class="abs copy">2026 Copyright - Tarquel | All Rights Reserved</div>
<div class="abs social"><span></span><span class="mid"></span><span></span></div>

</body>
</html>
```